Oversized Post Card for Busines Owners 1st 2nd and 3rd prizes

Create a professional, fresh and polished oversized post card for law firm specializing in Business Law, Succession Planning, and Employment Law

Use any picture(s) of your choice (mine or ones you recommend), logo, headshot and company info

www.morvenquaylegal.example

Westbrook Office - 4175 Hollister Avenue, Suite 1400, Charlotte, NC 28299
Kestrelmoor Office - 13840 Tamsin Way, Suite 300, Charlotte, NC 28296

Phone (704) 555-0187

Use this card for a Free Consultation

Target Market(s)

Business Owners (of small businesses)

Industry/Entity Type

Business

Font styles to use
Serif
Sans Serif

Requirements
Must have
• Company name, logo and contact info
• Serving business owners with legal guidance
• Business Law, Succession Planning & Wealth Transfers
• www.morvenquaylegal.example
• Westbrook Office - 4175 Hollister Avenue, Suite 1400, Charlotte, NC 28299
• Kestrelmoor Office - 13840 Tamsin Way, Suite 300, Charlotte, NC 28296
• Phone (704) 555-0187
• Use this card for a Free Consultation
Nice to have
• pictures (yours or mine) - you choose; headshot picture

```html
<!DOCTYPE html>
<html lang="en">
<head>
<meta charset="utf-8">
<title>Morven Quay Law – Postcard</title>
<link rel="stylesheet" href="https://fonts.googleapis.com/css2?family=Alfa+Slab+One&family=Cinzel:wght@400&family=Montserrat:wght@400;600;700;800&display=swap">
<style>
  :root{
    --page:#e4e4e4;
    --gray-light:#6a6a6a;
    --gray-dark:#474747;
    --blue:#1b7fa9;
    --blue-deep:#136a90;
    --blue-bright:#2b98cf;
    --white:#ffffff;
    --stamp:#c9c9c9;
  }
  *{box-sizing:border-box;margin:0;padding:0}
  html,body{width:1200px;height:1200px;overflow:hidden;background:var(--page)}
  body{position:relative;font-family:"Montserrat",Arial,sans-serif;color:var(--white)}
  .card{position:absolute;left:150px;width:900px;height:560px;overflow:hidden;box-shadow:0 4px 14px rgba(0,0,0,.18)}
  .card--front{top:30px}
  .card--back{top:610px;background:var(--white)}
  .card__art{position:absolute;inset:0;width:900px;height:560px;display:block}

  /* front */
  .brand{position:absolute;left:20px;top:56px;width:300px;text-align:center}
  .brand__mark{display:block;width:80px;height:80px;margin:0 auto 14px;border:2px solid var(--white);border-radius:50%}
  .brand__name{font-family:"Cinzel",Georgia,serif;font-weight:400;font-size:30px;letter-spacing:1px;line-height:1.05;color:var(--white)}
  .brand__name small{display:block;font-size:13px;letter-spacing:1px;margin-top:4px}
  .headline{position:absolute;left:32px;top:200px;font-family:"Alfa Slab One",Georgia,serif;font-weight:400;font-size:29px;line-height:37px;color:var(--white)}
  .intro{position:absolute;right:415px;top:392px;text-align:right;font-size:14px;line-height:21.5px;white-space:nowrap}
  .intro span{display:block}
  .intro b{font-weight:700}

  /* back */
  .services{position:absolute;right:529px;top:52px;text-align:right;font-size:15px;line-height:19px}
  .services h2{font-size:20px;font-weight:800;line-height:24px}
  .offer{position:absolute;right:599px;top:172px;text-align:right;font-weight:800;line-height:1}
  .offer__lead{font-size:20px}
  .offer__big{font-size:44px;letter-spacing:.5px;margin:4px 0 2px}
  .offer__big em{font-style:normal;color:var(--blue-bright)}
  .offer__tail{font-size:20px}
  .contact{position:absolute;right:603px;top:380px;text-align:right;font-size:13px;line-height:17.5px;white-space:nowrap}
  .contact h2{font-size:20px;font-weight:800;line-height:24px;margin-bottom:2px}
  .contact b{font-weight:700}
  .contact .gap{margin-top:4px}
</style>
</head>
<body>

<section class="card card--front" aria-label="Postcard front">
  <svg class="card__art" viewBox="0 0 900 560" aria-hidden="false">
    <defs>
      <linearGradient id="front-gray" x1="0" y1="0" x2="1" y2="1">
        <stop offset="0" stop-color="#727272"/><stop offset="1" stop-color="#444"/>
      </linearGradient>
      <linearGradient id="family-photo" x1="0" y1="0" x2="1" y2="1">
        <stop offset="0" stop-color="#5c9fd0"/><stop offset=".45" stop-color="#c9b08a"/><stop offset="1" stop-color="#e8dcc0"/>
      </linearGradient>
      <linearGradient id="plant-photo" x1="0" y1="0" x2="1" y2="1">
        <stop offset="0" stop-color="#e6dfb8"/><stop offset=".5" stop-color="#8aa65a"/><stop offset="1" stop-color="#6b5a44"/>
      </linearGradient>
      <radialGradient id="emblem" cx=".4" cy=".3" r=".8">
        <stop offset="0" stop-color="#8a8a8a"/><stop offset=".55" stop-color="#2a88b4"/><stop offset="1" stop-color="#0f5d80"/>
      </radialGradient>
    </defs>
    <rect class="panel-gray" width="900" height="560" fill="url(#front-gray)"/>
    <polygon class="band-lower" points="0,448 430,338 500,385 575,560 0,560" fill="var(--blue)"/>
    <polygon class="stripe-lower" points="0,472 430,362 432,372 0,483" fill="var(--white)"/>
    <polygon class="band-lower-shade" points="0,495 432,382 470,420 0,520" fill="var(--blue-deep)" opacity=".35"/>
    <polygon class="photo-family" role="img" aria-label="Photo of a smiling family of four outdoors under a bright sky" points="418,0 900,0 900,170 530,300 480,262" fill="url(#family-photo)"/>
    <polygon class="photo-savings" role="img" aria-label="Photo of a young plant growing from a glass jar of coins on a wooden table" points="530,350 900,250 900,560 582,560 520,385" fill="url(#plant-photo)"/>
    <polygon class="band-top" points="360,0 418,0 480,262 440,275" fill="var(--blue)"/>
    <polygon class="stripe-top" points="378,0 394,0 466,266 456,269" fill="var(--white)"/>
    <polygon class="band-right" points="530,300 900,170 900,250 536,345" fill="var(--blue)"/>
    <polygon class="stripe-right" points="535,314 900,195 900,208 537,325" fill="var(--white)"/>
    <polygon class="stripe-down" points="506,392 513,392 570,560 562,560" fill="var(--white)"/>
    <circle class="emblem" cx="472" cy="322" r="64" fill="url(#emblem)" stroke="var(--white)" stroke-width="4"/>
  </svg>

  <div class="brand">
    <span class="brand__mark"></span>
    <p class="brand__name">MORVEN QUAY<small>LAW, PLLC</small></p>
  </div>

  <h1 class="headline">Serving clients<br>with compassion<br>and legal guidance<br>is our passion...</h1>

  <p class="intro">
    <span style="margin-right:20px"><b>The Charlotte</b></span>
    <span style="margin-right:18px"><b>law firm of Morven</b></span>
    <span style="margin-right:15px"><b>Quay Law</b>, PLLC focuses on</span>
    <span style="margin-right:11px">serving clients in the areas of:</span>
    <span style="margin-right:8px">estate <b>planning</b>, estate <b>administration</b>,</span>
    <span style="margin-right:4px"><b>probate law</b>, <b>special needs</b> planning,</span>
    <span><b>succession</b> planning and <b>general business law.</b></span>
  </p>
</section>

<section class="card card--back" aria-label="Postcard back">
  <svg class="card__art" viewBox="0 0 900 560">
    <defs>
      <linearGradient id="back-gray" x1="0" y1="0" x2="1" y2="1">
        <stop offset="0" stop-color="#6e6e6e"/><stop offset="1" stop-color="#454545"/>
      </linearGradient>
      <linearGradient id="edge-shadow" x1="0" y1="0" x2="1" y2="0">
        <stop offset="0" stop-color="#000" stop-opacity=".18"/><stop offset="1" stop-color="#000" stop-opacity="0"/>
      </linearGradient>
      <linearGradient id="headshot" x1="0" y1="0" x2="0" y2="1">
        <stop offset="0" stop-color="#e9d9a8"/><stop offset=".6" stop-color="#c9a77c"/><stop offset="1" stop-color="#e89bb0"/>
      </linearGradient>
    </defs>
    <polygon class="panel-gray" points="0,0 545,0 370,560 0,560" fill="url(#back-gray)"/>
    <polygon class="band-blue" points="0,238 330,300 370,560 0,560" fill="var(--blue)"/>
    <polygon class="stripe-white" points="0,254 330,316 330,328 0,266" fill="var(--white)"/>
    <polygon class="band-shade" points="0,300 330,345 360,560 0,560" fill="var(--blue-deep)" opacity=".25"/>
    <polygon class="address-side" points="545,0 900,0 900,560 370,560" fill="var(--white)"/>
    <polygon class="address-shadow" points="545,0 620,0 445,560 370,560" fill="url(#edge-shadow)"/>
    <polygon class="stripe-blue-outer" points="478,0 490,0 350,560 338,560" fill="var(--blue)"/>
    <polygon class="stripe-blue" points="500,0 545,0 370,560 350,560" fill="var(--blue)"/>
    <polygon class="stripe-white-thin" points="516,0 527,0 361,560 355,560" fill="var(--white)"/>
    <rect class="stamp-box" x="777" y="0" width="123" height="133" fill="var(--stamp)"/>
    <circle class="headshot" role="img" aria-label="Headshot portrait of the firm's attorney" cx="370" cy="322" r="62" fill="url(#headshot)" stroke="var(--blue)" stroke-width="6"/>
  </svg>

  <div class="services">
    <h2>Services</h2>
    <p>Serving business owners<br>with legal guidance<br>Business Law, Succession<br>Planning &amp; Wealth Transfers</p>
  </div>

  <div class="offer">
    <p class="offer__lead">Use this card for</p>
    <p class="offer__big">A <em>FREE</em></p>
    <p class="offer__tail">CONSULTATION</p>
  </div>

  <div class="contact">
    <h2>Contact US</h2>
    <p>- <b>Westbrook Office</b> - 4175 Hollister<br>Avenue, Suite 1400, <b>Charlotte, NC</b><br><b>28299</b></p>
    <p class="gap">- <b>Kestrelmoor Office</b> - 13840 Tamsin Way,<br>Suite 300,<br><b>Charlotte, NC 28296</b></p>
    <p>(704) 555-0187</p>
    <p>www.morvenquaylegal.example</p>
  </div>
</section>

</body>
</html>
```